Business Card Design Project

I want my business cards to stand and feel timeless! I also want people to get their hands on them and freak out over how cool these are, I already have a logo i just want a very cool card design! this is for a makeup artist and maybe one day a line of cosmetics.

Target Market(s)

I want this to target women from 18 to 45

Industry/Entity Type

Business

Font styles to use
Decorative
Script

Colors

Designer to choose colors to be used in the design.

Requirements
Must have
• it must be elegante

```html
<!DOCTYPE html>
<html lang="en">
<head>
<meta charset="UTF-8">
<title>Mara Quinn — Business Card</title>
<link rel="stylesheet" href="https://fonts.googleapis.com/css2?family=Montserrat:wght@300;400&family=Pinyon+Script&display=swap">
<style>
  :root {
    --stage: #2a2624;
    --card: #0c0c0c;
    --card-edge: #1a1a1a;
    --ink-silver: #e6e6e6;
    --ink-muted: #cfcfcf;
    --ink-deboss: #262626;
    --rule: #bdbdbd;
  }
  * { margin: 0; padding: 0; box-sizing: border-box; }
  html, body {
    width: 1200px;
    height: 716px;
    overflow: hidden;
    background: var(--stage);
  }
  .canvas {
    position: relative;
    width: 1200px;
    height: 716px;
    display: flex;
    align-items: center;
    justify-content: center;
    gap: 60px;
  }
  .card {
    position: relative;
    width: 490px;
    height: 280px;
    background: var(--card);
    border: 1px solid var(--card-edge);
    border-radius: 3px;
    font-family: "Montserrat", Arial, sans-serif;
    color: var(--ink-silver);
  }
  /* Front */
  .card-front {
    display: flex;
    align-items: center;
    justify-content: center;
  }
  .brand-name {
    font-family: "Montserrat", Arial, sans-serif;
    font-weight: 300;
    font-size: 46px;
    letter-spacing: 6px;
    color: var(--ink-deboss);
    text-transform: uppercase;
    line-height: 1;
  }
  /* Back */
  .identity {
    position: absolute;
    top: 52px;
    left: 0;
    right: 0;
    text-align: center;
    padding-left: 90px;
  }
  .person-name {
    font-family: "Pinyon Script", "Brush Script MT", cursive;
    font-size: 44px;
    line-height: 1;
    color: var(--ink-silver);
  }
  .person-title {
    margin-top: 4px;
    margin-right: 70px;
    font-size: 11px;
    letter-spacing: 1.5px;
    color: var(--ink-muted);
  }
  .details {
    position: absolute;
    top: 170px;
    left: 0;
    right: 0;
    display: flex;
    justify-content: center;
    font-size: 12px;
    line-height: 20px;
    letter-spacing: 0.3px;
  }
  .contact-list {
    list-style: none;
    text-align: right;
    padding-right: 14px;
  }
  .contact-label { display: inline-block; width: 26px; text-align: right; }
  .details-divider {
    width: 1px;
    background: var(--rule);
  }
  .address {
    font-style: normal;
    padding-left: 14px;
  }
</style>
</head>
<body>
  <main class="canvas">
    <section class="card card-front" aria-label="Card front">
      <div class="brand-name">Mara Quinn</div>
    </section>

    <section class="card card-back" aria-label="Card back">
      <div class="identity">
        <div class="person-name">Mara Quinn</div>
        <div class="person-title">GENERAL DIRECTOR</div>
      </div>
      <div class="details">
        <ul class="contact-list">
          <li>800 555 0147 <span class="contact-label">[P]</span></li>
          <li>mara@maraquinn.com <span class="contact-label">[E]</span></li>
          <li>www.maraquinn.com <span class="contact-label">[W]</span></li>
        </ul>
        <div class="details-divider"></div>
        <address class="address">
          4120 Larkspur Ave NE<br>
          Suite 200, Building , Oregon<br>
          USA 97035
        </address>
      </div>
    </section>
  </main>
</body>
</html>
```